8 new icons - bootstrap feel (no 3d)

I am redesigning http://www.brightlanepanels.com with bootstrap (go figure).. ;-)
You can see a preview here:
brightlanepanels[dot]com/bs/index[dot]html
(sorry for the [dot]'s, I don't want this to get indexed by vexlo)
I am looking for 8 new icons that will match the current color/design that I have already started. You can see the filler images to see where they will go.
- I would like them to be big enough for mobile
- No 3D
- Grab colors/style from new site
- Take a look at bootstrap's 3 icons here: http://plimora.repohive.com/framekit/
- Icons should be flat or have a gradient like bootstraps above.
- The circuit board pattern is not needed for these icons.
If you don't know much about the printed circuit board industry, the first four (quick turn, prototype, production, ad multilayer) could be a little tricky, but, I believe after you read the descriptions and vexlo them, you can come with some ideas.
Ideas:
- Quick turn, you could have "24 hours" in the middle with an arrow around them to represent the "turn around".
- Prototype PCBs are for low quantities, so you could have just one to five PCBs there.
- Production PCBs are for higher volumes, so having arrows going up or A LOT of PCBs would work.
- Multilayer PCBs are a multi layered printed circuit board, so having a board that shows the different layers would work great. You can vexlo multialyer pcb and find some inspiration as well.
The other four (aerospace/military, medial/bio-medial, industrial/automotive, and students/hobbyist) seem to me to be really straight forward, so, I won't go into details about those. Be creative. :-)

```html
<!DOCTYPE html>
<html lang="en">
<head>
<meta charset="utf-8">
<title>Bright Lane Panels</title>
<link href="https://fonts.googleapis.com/css2?family=Arimo:wght@400;700&display=swap" rel="stylesheet">
<style>
  :root {
    --page-bg: #e9e9e9;
    --panel-bg: #ffffff;
    --footer-bg: #cacaca;
    --card-border: #dcdcdc;
    --text: #555555;
    --heading: #464646;
    --footer-text: #2b2b2b;
    --partner: #7a7a7a;
    --icon-light: #8f8a00;
    --icon-dark: #1f4a02;
    --marker: #9a9a9a;
  }
  * { box-sizing: border-box; margin: 0; padding: 0; }
  html, body { width: 1200px; height: 589px; overflow: hidden; }
  body {
    position: relative;
    background: var(--page-bg);
    font-family: "Arimo", Arial, sans-serif;
    font-size: 17.5px;
    line-height: 25.3px;
    color: var(--text);
  }
  .content {
    position: absolute; left: 6px; top: 0; width: 1189px; height: 515px;
    background: var(--panel-bg);
  }
  .service-card {
    position: absolute; top: -40px; height: 212px;
    border: 1px solid var(--card-border); border-radius: 5px;
    background: var(--panel-bg);
    padding: 30px 0 0 18px;
  }
  .service-card.production { left: 19px; width: 374px; }
  .service-card.multilayer { left: 409px; width: 374px; }
  .section-title {
    position: absolute; font-size: 25px; font-weight: 700; color: var(--heading);
    line-height: 30px;
  }
  .markets-title { left: 19px; top: 221px; }
  .market-card {
    position: absolute; top: 274px; width: 178px; height: 203px;
    border: 1px solid var(--card-border); border-radius: 5px; background: var(--panel-bg);
  }
  .market-art {
    position: absolute; left: 26px; top: 7px; width: 124px; height: 112px;
    border-radius: 6px;
    background: linear-gradient(135deg, var(--icon-light), var(--icon-dark));
  }
  .market-labels {
    position: absolute; left: 20px; top: 135px;
    font-weight: 700; line-height: 22px; list-style: none;
  }
  .market-labels li { position: relative; padding-left: 24px; }
  .market-labels li::before {
    content: ""; position: absolute; left: 0; top: 5px; width: 12px; height: 12px;
    border: 1px solid var(--marker);
  }
  .partners { position: absolute; left: 829px; top: 0; width: 350px; height: 210px; }
  .partner {
    position: absolute; color: var(--partner); font-weight: 700; white-space: nowrap;
    display: flex; align-items: center; gap: 6px;
  }
  .partner .dot { width: 22px; height: 22px; border-radius: 50%; background: var(--partner); }
  .partner .sq { width: 18px; height: 18px; background: var(--partner); }
  .more { position: absolute; right: 19px; top: 215px; }
  .mission-title { left: 835px; top: 262px; }
  .mission-text { position: absolute; left: 835px; top: 316px; width: 355px; }
  .site-footer {
    position: absolute; left: 0; top: 515px; width: 1200px; height: 74px;
    background: var(--footer-bg); color: var(--footer-text);
  }
  .site-footer p { position: absolute; left: 6px; }
  .site-footer .credit { top: 10px; }
  .site-footer .license { top: 48px; }
  .site-footer .to-top { left: auto; right: 5px; top: 10px; }
</style>
</head>
<body>
  <main class="content">
    <section class="service-card production">
      <p>We provide production quantity PCBs at<br>competitive go-to-market pricing with no<br>NRE mins or contracts. We can<br>manufacture your production run in-house<br>or through one of our network of PCB<br>partners overseas.</p>
    </section>
    <section class="service-card multilayer">
      <p>We have the capabilities to manufacture<br>printed circuit boards with 2 to 24 layers.<br>Our maximum board size for multilayer<br>PCBs is 16"x26" and the standard<br>turnaround time depends on the<br>complexity of the board.</p>
    </section>

    <h2 class="section-title markets-title">PCB Markets</h2>

    <article class="market-card" style="left:19px">
      <div class="market-art" role="img" aria-label="Fighter jet silhouette icon"></div>
      <ul class="market-labels"><li>Aerospace.</li><li>Military.</li></ul>
    </article>
    <article class="market-card" style="left:214px">
      <div class="market-art" role="img" aria-label="Microscope silhouette icon"></div>
      <ul class="market-labels"><li>Medical.</li><li>Bio-Medical.</li></ul>
    </article>
    <article class="market-card" style="left:409px">
      <div class="market-art" role="img" aria-label="Tractor silhouette icon"></div>
      <ul class="market-labels"><li>Industrial.</li><li>Automotive.</li></ul>
    </article>
    <article class="market-card" style="left:605px">
      <div class="market-art" role="img" aria-label="Graduate in cap silhouette icon"></div>
      <ul class="market-labels"><li>Students.</li><li>Hobbyist.</li></ul>
    </article>

    <div class="partners">
      <span class="partner" style="left:75px;top:0;font-size:22px">Halvane</span>
      <span class="partner" style="left:210px;top:-2px;font-size:24px"><span class="dot"></span>oreta</span>
      <span class="partner" style="left:50px;top:64px;font-size:22px"><span class="sq"></span>Tavik</span>
      <span class="partner" style="left:165px;top:64px;font-size:22px">Quintara</span>
      <span class="partner" style="left:35px;top:122px;font-size:22px">Nolmark</span>
      <span class="partner" style="left:160px;top:122px;font-size:15px">Osmera Semi<span class="dot"></span></span>
      <span class="partner" style="left:101px;top:172px;font-size:22px"><span class="sq"></span>Kestrova</span>
    </div>
    <p class="more">and many more...</p>

    <h2 class="section-title mission-title">Our Mission.</h2>
    <p class="mission-text">To manufacture and deliver high-quality<br>printed circuit boards on time at a<br>competitive price with industry leading<br>customer service that is staffed by printed<br>circuit board professionals that exceed our<br>customer's expectations and goals.</p>
  </main>

  <footer class="site-footer">
    <p class="credit">Designed and built with all the love in the world @loomhub by @ravn and @jeli.</p>
    <p class="to-top">Back to top</p>
    <p class="license">Code licensed under the Apache License v2.0. Documentation licensed under CC BY 3.0.</p>
  </footer>
</body>
</html>
```